Artwork for pharmaceutical cream against eczema

We are a Belgian company launching a steroid-free cream for itchy, red and eczematic skin. It will be a 50 ml tube in a cardboard box. We are looking for a reliable, pharmaceutical, yet no sterile clinical, feel. A product a pharmacist would recommend, but you would not find in a general drug store or perfume shop. The name of the product is "Vumero". Colors to be used are deep blue, orange, black and white. The main color should not be black or white. The prominent use of the capital "S", like in the Drenoxa example should be considered. A design with a curved element that goes with the S, like in the Vitamin C example has the preference.

Reason: Hi all, I will extend the deadline with 5 days, because we feel that there is still not a perfect fit. Thanks Koen

Target Market(s)

Pharmacy. Broad public. Young parents with growing children.

Industry/Entity Type

Pharmacy

Font styles to use
Sans Serif

Requirements
Must have
• Text elements:
• "Vumero® crème"
• "50 g"
• "Bevat 1% hatseflats"
• "Verzorging van jeukende, rode en geïrriteerde huid"
Nice to have
• Side text elements (in plain black):
• "Lot 17XX17"
• "EXP 04/2020"
• Dummy EAN-13 barcode
• "Durno bvba - Vumerostraat 15 - 1234 Antwerpen"
• "Bevat Lorem ipsum dolor sit amet, consectetur adipiscing elit, sed do eiusmod tempor incididunt ut labore et dolore magna aliqua"

```html
<!DOCTYPE html>
<html lang="nl">
<head>
<meta charset="utf-8">
<title>Vumero crème – verpakking voorzijde</title>
<link rel="stylesheet" href="https://fonts.googleapis.com/css2?family=Open+Sans:wght@400;700&display=swap">
<style>
  :root {
    --page: #ffffff;
    --deep-blue: #1616c8;
    --royal-blue: #2a35d8;
    --sky-blue: #5c8ef0;
    --pale-blue: #a9c6fa;
    --orange: #f5a53a;
    --white: #ffffff;
  }
  * { margin: 0; padding: 0; box-sizing: border-box; }
  html, body {
    width: 1200px;
    height: 642px;
    overflow: hidden;
    background: var(--page);
    font-family: "Open Sans", sans-serif;
  }
  .box-front {
    position: absolute;
    left: 40px;
    top: 192px;
    width: 1120px;
    height: 258px;
    overflow: hidden;
    background: linear-gradient(90deg, var(--deep-blue) 0%, var(--royal-blue) 55%, #3b3fe0 100%);
  }
  .wave {
    position: absolute;
    left: 0;
    top: 0;
    width: 100%;
    height: 100%;
  }
  .initial-block {
    position: absolute;
    left: 110px;
    top: 12px;
    width: 210px;
    height: 216px;
    background: var(--orange);
  }
  .product-name {
    position: absolute;
    left: 470px;
    top: 26px;
    font-size: 42px;
    font-weight: 700;
    line-height: 1.1;
    color: var(--white);
    white-space: nowrap;
  }
  .product-name .brand sup {
    font-size: 16px;
    font-weight: 400;
    vertical-align: 22px;
    margin-left: 2px;
  }
  .product-name .form {
    color: var(--orange);
    margin-left: 12px;
  }
  .net-content {
    position: absolute;
    left: 472px;
    top: 98px;
    font-size: 25px;
    line-height: 1.3;
    color: var(--white);
  }
  .claims {
    position: absolute;
    left: 472px;
    top: 154px;
    font-size: 19px;
    line-height: 28px;
    color: var(--white);
    white-space: nowrap;
  }
  .seal {
    position: absolute;
    left: 916px;
    top: 78px;
    width: 64px;
    height: 64px;
    border: 3px solid var(--white);
    border-radius: 50%;
  }
  .rule-horizontal {
    position: absolute;
    left: 0;
    right: 0;
    top: 232px;
    height: 4px;
    background: var(--orange);
  }
  .rule-vertical {
    position: absolute;
    top: 0;
    bottom: 0;
    width: 4px;
    background: var(--orange);
  }
  .rule-vertical.inner { left: 1072px; }
  .rule-vertical.outer { left: 1086px; }
</style>
</head>
<body>
  <section class="box-front" aria-label="Vumero crème verpakking">
    <svg class="wave" viewBox="0 0 1120 258" preserveAspectRatio="none" aria-hidden="true">
      <path d="M0 130 C 260 100, 520 190, 760 180 C 900 174, 1020 190, 1120 200 L1120 258 L0 258 Z" fill="var(--sky-blue)" opacity="0.8"/>
      <path d="M0 180 C 300 160, 560 230, 1120 226 L1120 258 L0 258 Z" fill="var(--pale-blue)" opacity="0.7"/>
    </svg>

    <div class="initial-block" role="img" aria-label="Groot oranje merkvlak"></div>

    <h1 class="product-name"><span class="brand">Vumero<sup>®</sup></span><span class="form">crème</span></h1>
    <p class="net-content">50 g</p>
    <p class="claims">Bevat 1% hatseflats<br>Verzorging van jeukende, rode en geïrriteerde huid</p>

    <div class="seal" aria-hidden="true"></div>

    <div class="rule-horizontal"></div>
    <div class="rule-vertical inner"></div>
    <div class="rule-vertical outer"></div>
  </section>
</body>
</html>
```